Flyer design for the Harvest Lantern Summit 2019 (HALSUM)

Design a flyer for our annual conference with basic information about the conference: conference logo and year, Conference name: Harvest Lantern Summit Location: Talbot Community Center (Downtown Portland)482 Wexley Street, Portland, ME 04109, Date: August 8th, 9th, 10th and 11th, 2019Start time 7:00PMI would like the following three words added to the flyer. These words describe the vision of the conference: Prophetic, Fire, Overflow,

Contact info:
Website: www.vostel.org
Phone: 207 555 3184
Email: contact@meadowcrest.org

Target Market(s)

Young adults living in the United States

Industry/Entity Type

Religious

Font styles to use
Sans Serif

Colors

Designer to choose colors to be used in the design.

Requirements
Must have
• HALSUM must logo standout, the reader should be able to take a quick look and find key info,
Should not have
• Cross image, church image

```html
<!DOCTYPE html>
<html lang="en">
<head>
<meta charset="utf-8">
<title>Harvest Lantern Summit 2019 — Flyer</title>
<link rel="stylesheet" href="https://fonts.googleapis.com/css2?family=Montserrat:wght@700;800&family=Oswald:wght@500&family=Arvo:wght@400;700&display=swap">
<style>
  :root {
    --brand-blue: #1a6fb8;
    --band-blue: #156bb3;
    --brand-orange: #f39a21;
    --flame-light: #f6a93a;
    --flame-deep: #e8392a;
    --ink: #1c1c1c;
    --paper: #ffffff;
    --paper-shade: #f1f1f1;
    --backdrop: #cfcdc6;
  }
  * { box-sizing: border-box; margin: 0; padding: 0; }
  html, body { width: 1200px; height: 1200px; overflow: hidden; }
  body { background: var(--backdrop); position: relative; }

  .flyer {
    position: absolute; left: 200px; top: 40px;
    width: 800px; height: 1120px;
    background: var(--paper);
    overflow: hidden;
    box-shadow: 0 6px 24px rgba(0,0,0,.12);
  }
  .flyer__wave { position: absolute; inset: 0; width: 100%; height: 100%; }

  .flame-art {
    position: absolute; left: 520px; top: 300px;
    width: 230px; height: 560px;
    border-radius: 50% 50% 45% 45% / 70% 70% 30% 30%;
    background: linear-gradient(170deg, var(--flame-light) 0%, #f0782a 60%, var(--flame-deep) 100%);
  }

  .logo { position: absolute; left: 70px; top: 120px; }
  .logo__name {
    font-family: "Montserrat", sans-serif; font-weight: 800;
    font-size: 96px; line-height: 1; color: var(--brand-blue); letter-spacing: 1px;
  }
  .logo__year {
    display: flex; align-items: center; gap: 14px; margin-top: 4px;
    font-family: "Montserrat", sans-serif; font-weight: 700;
    font-size: 34px; color: var(--brand-orange); letter-spacing: 18px;
  }
  .logo__year::before, .logo__year::after {
    content: ""; height: 3px; background: var(--brand-orange); flex: none;
  }
  .logo__year::before { width: 90px; }
  .logo__year::after { width: 100px; }

  .headline {
    position: absolute; left: 70px; top: 300px;
    font-family: "Montserrat", sans-serif; font-weight: 800;
    font-size: 40px; line-height: 1.2; color: var(--brand-orange); text-transform: uppercase;
  }

  .vision { position: absolute; left: 70px; top: 440px; list-style: none; }
  .vision__item { display: flex; align-items: center; margin-bottom: 12px; }
  .vision__icon { width: 48px; height: 48px; margin-right: 16px; }
  .vision__tag {
    background: var(--brand-orange); color: var(--paper);
    font-family: "Oswald", sans-serif; font-weight: 500;
    font-size: 40px; line-height: 1; padding: 10px 26px; text-transform: uppercase;
  }

  .dates { position: absolute; left: 80px; top: 690px; color: var(--brand-blue); }
  .dates__month { font-family: "Montserrat", sans-serif; font-weight: 800; font-size: 40px; line-height: 1.2; }
  .dates__days { font-family: "Arvo", serif; font-weight: 700; font-size: 30px; line-height: 1.25; margin-top: 4px; }
  .dates__time { font-family: "Arvo", serif; font-weight: 700; font-size: 30px; line-height: 1.25; margin-top: 30px; }

  .venue {
    position: absolute; left: 80px; top: 866px;
    font-family: "Arvo", serif; font-weight: 700; font-style: normal;
    font-size: 26px; line-height: 1.22; color: var(--ink);
  }

  .contact-band {
    position: absolute; left: 0; bottom: 0; width: 100%; height: 82px;
    background: var(--band-blue); color: var(--paper);
    display: flex; align-items: center; justify-content: space-between; padding: 0 40px;
    font-family: "Arvo", serif; font-size: 22px;
  }
  .contact-band__item { display: flex; align-items: center; gap: 10px; }
  .contact-band__icon { width: 24px; height: 24px; }
</style>
</head>
<body>
  <main class="flyer">
    <svg class="flyer__wave" viewBox="0 0 800 1120" aria-hidden="true">
      <path d="M0 0 H520 C640 120 580 320 500 480 C420 640 470 860 560 1120 H0 Z" fill="var(--paper-shade)"/>
    </svg>

    <div class="flame-art" role="img" aria-label="Large stylised orange flame illustration"></div>

    <header class="logo">
      <div class="logo__name">HALSUM</div>
      <div class="logo__year">2019</div>
    </header>

    <h1 class="headline">Harvest Lantern<br>Summit</h1>

    <ul class="vision">
      <li class="vision__item">
        <svg class="vision__icon" viewBox="0 0 48 48" aria-hidden="true"><path d="M24 42 C6 30 4 18 12 12 C18 8 22 12 24 16 C26 12 30 8 36 12 C44 18 42 30 24 42 Z" fill="var(--brand-orange)"/></svg>
        <span class="vision__tag">Prophetic</span>
      </li>
      <li class="vision__item">
        <svg class="vision__icon" viewBox="0 0 48 48" aria-hidden="true"><g fill="none" stroke="var(--brand-orange)" stroke-width="3"><rect x="8" y="24" width="30" height="14"/><path d="M12 30h22M12 34h22M14 20l6-10M22 20l8-8M30 22l8-4"/></g></svg>
        <span class="vision__tag">Overflow</span>
      </li>
      <li class="vision__item">
        <svg class="vision__icon" viewBox="0 0 48 48" aria-hidden="true"><path d="M24 4 C28 14 38 20 38 30 C38 38 32 44 24 44 C16 44 10 38 10 30 C10 22 16 20 18 12 C22 18 22 22 24 26 C28 20 26 12 24 4 Z" fill="var(--brand-orange)"/></svg>
        <span class="vision__tag">Fire</span>
      </li>
    </ul>

    <section class="dates">
      <div class="dates__month">AUGUST 2019</div>
      <div class="dates__days">8th, 9th, 10th and 11th</div>
      <div class="dates__time">Start time 7:00PM</div>
    </section>

    <address class="venue">
      Talbot Community<br>Center<br>(Downtown Portland)<br>482 Wexley Street,<br>Portland, ME 04109
    </address>

    <footer class="contact-band">
      <span class="contact-band__item">
        <svg class="contact-band__icon" viewBox="0 0 24 24" aria-hidden="true"><path d="M6 2l4 4-2 3c1 3 4 6 7 7l3-2 4 4-3 4C10 22 2 14 2 5z" fill="var(--paper)"/></svg>
        207 555 3184
      </span>
      <span class="contact-band__item">
        <svg class="contact-band__icon" viewBox="0 0 24 24" aria-hidden="true"><g fill="none" stroke="var(--paper)" stroke-width="2"><rect x="2" y="5" width="20" height="14"/><path d="M2 5l10 8 10-8"/></g></svg>
        contact@meadowcrest.org
      </span>
      <span class="contact-band__item">
        <svg class="contact-band__icon" viewBox="0 0 24 24" aria-hidden="true"><g fill="none" stroke="var(--paper)" stroke-width="1.8"><circle cx="12" cy="12" r="10"/><ellipse cx="12" cy="12" rx="4.5" ry="10"/><path d="M2 12h20M4 7h16M4 17h16"/></g></svg>
        www.vostel.org
      </span>
    </footer>
  </main>
</body>
</html>
```